Bref créative
Stationary for a Home Builder
Calvin Morrow
Professional
Calvin Morrow, MBA
Owner
4827 Pelham Crescent
Edmonton, AB
T6R 2J8
calvin@rpbbuilds.com
rpbbuilds.com
For the business card you may want to delete the 'rpbbuilds.com' at the bottom which is currently on the AI file provided.
I'd like to have the logo on the back of the card with enough white space to allow hand written notes to be added.
Logo - White and Blue - AI
Logo - White and Blue - EPS
Logo - Black and Blue - AI
Logo - Black and Blue - EPS

```html
<!DOCTYPE html>
<html lang="en">
<head>
<meta charset="utf-8">
<title>RPB Builds Stationery</title>
<link href="https://fonts.googleapis.com/css2?family=Montserrat:wght@700&family=Open+Sans:wght@400;600;700&display=swap" rel="stylesheet">
<style>
:root{
  --bg:#8c8c8c;
  --bg-light:#a4a4a4;
  --paper:#ffffff;
  --blue:#1f6fb8;
  --ink:#1a1a1a;
  --grey-text:#555;
  --label:#f2f2f2;
}
*{margin:0;padding:0;box-sizing:border-box}
html,body{width:1200px;height:568px;overflow:hidden}
body{background:radial-gradient(ellipse at 60% 45%,var(--bg-light),var(--bg));font-family:"Open Sans",Arial,sans-serif;position:relative}
.piece{position:absolute;background:var(--paper);box-shadow:0 2px 6px rgba(0,0,0,.35);overflow:hidden}
.piece-label{position:absolute;color:var(--label);font-size:7px;text-align:center;white-space:nowrap}
.wordmark{font-family:"Montserrat",Arial,sans-serif;font-weight:700;color:var(--ink);line-height:1}
.art{position:absolute;left:0;top:0}
/* sign */
.sign{left:48px;top:43px;width:317px;height:509px}
.sign .wordmark{position:absolute;left:28px;top:40px;font-size:92px;letter-spacing:-2px}
.sign .wordmark span{display:block;font-size:40px;letter-spacing:10px;margin-top:10px;padding-left:6px}
.sign-call{position:absolute;left:20px;top:290px;transform:rotate(-12deg);transform-origin:left top;font-weight:700;color:var(--ink);line-height:1.05}
.sign-call .call{font-size:25px}
.sign-call .phone{font-size:31px}
.sign-fields{position:absolute;left:18px;top:400px;width:270px;color:#fff;font-size:15px}
.field{display:flex;align-items:flex-end;height:31px}
.field .rule{flex:1;border-bottom:1.5px solid #fff;margin:0 6px 4px}
.sign-url{position:absolute;right:14px;bottom:12px;color:#fff;font-size:10px;font-weight:700}
/* letter size sheets */
.sheet{top:209px;width:221px;height:324px}
.work-order{left:427px}
.letterhead{left:672px}
.sheet .wordmark{position:absolute;left:12px;top:14px;font-size:20px}
.sheet-address{position:absolute;right:12px;top:16px;font-size:4px;line-height:1.5;color:var(--grey-text);text-align:left}
.sheet-url{position:absolute;right:8px;bottom:5px;font-size:4.5px;color:#fff;font-weight:600}
.order-table{position:absolute;left:12px;top:56px;width:160px;border-collapse:collapse;font-size:4px;color:var(--grey-text)}
.order-table td{border:.6px solid #999;height:9px;padding:0 2px}
.order-table td.head{width:38px}
.order-checks{position:absolute;left:12px;top:138px;display:flex;gap:8px;font-size:4px;color:var(--grey-text)}
.order-checks span::before{content:"";display:inline-block;width:4px;height:4px;border:.6px solid #777;margin-right:2px;vertical-align:-1px}
/* cards */
.card-v{top:89px;width:60px;height:108px}
.card-front{left:732px}
.card-back{left:799px}
.card-v .wordmark{position:absolute;left:6px;top:10px;font-size:11px}
.card-back .wordmark{left:0;right:0;text-align:center;top:14px}
.card-text{position:absolute;left:6px;top:34px;font-size:3.6px;line-height:1.5;color:var(--grey-text)}
.card-text b{color:var(--ink);font-size:4.2px}
.signature{left:888px;top:89px;width:168px;height:62px}
.signature .wordmark{position:absolute;left:8px;top:22px;font-size:15px}
.signature .card-text{left:8px;top:6px}
/* mail */
.label{left:924px;top:257px;width:132px;height:74px}
.label .wordmark{position:absolute;left:8px;top:8px;font-size:12px}
.label .card-text{left:8px;top:24px}
.envelope{left:924px;top:360px;width:132px;height:113px}
.envelope .wordmark{position:absolute;left:8px;top:8px;font-size:12px}
.envelope .card-text{left:8px;top:24px}
</style>
</head>
<body>

<div class="piece-label" style="left:48px;top:20px;width:317px">Sign (24" x 36")</div>
<section class="piece sign">
  <svg class="art" width="317" height="509" viewBox="0 0 317 509">
    <polygon points="120,268 317,205 317,268" fill="var(--blue)"/>
    <polygon points="0,380 317,312 317,509 0,509" fill="var(--blue)"/>
  </svg>
  <div class="wordmark">RPB<span>BUILDS</span></div>
  <div class="sign-call"><div class="call">Calls Us Today !</div><div class="phone">780.555.0148</div></div>
  <div class="sign-fields">
    <div class="field">Address<span class="rule"></span></div>
    <div class="field">Lot<span class="rule"></span>Block<span class="rule"></span></div>
    <div class="field">Job #<span class="rule"></span></div>
  </div>
  <div class="sign-url">rpbbuilds.com</div>
</section>

<div class="piece-label" style="left:427px;top:197px;width:221px">Work Order</div>
<section class="piece sheet work-order">
  <svg class="art" width="221" height="324" viewBox="0 0 221 324">
    <polygon points="150,300 221,262 221,324 130,324" fill="var(--blue)"/>
    <polygon points="170,290 221,262 221,268 178,291" fill="#fff"/>
  </svg>
  <div class="wordmark">RPB Builds</div>
  <div class="sheet-address">Calvin Morrow, MBA<br>4827 Pelham Crescent<br>Edmonton, AB T6R 2J8<br>calvin@rpbbuilds.com</div>
  <table class="order-table">
    <tr><td class="head">Date</td><td></td></tr>
    <tr><td class="head">Name</td><td></td></tr>
    <tr><td class="head">Address</td><td></td></tr>
    <tr><td class="head">Lot / Block</td><td></td></tr>
    <tr><td class="head">Job #</td><td></td></tr>
    <tr><td class="head">Notes</td><td></td></tr>
  </table>
  <div class="order-checks"><span>Framing</span><span>Electrical</span><span>Plumbing</span><span>Drywall</span><span>Finishing</span></div>
  <div class="sheet-url">rpbbuilds.com</div>
</section>

<div class="piece-label" style="left:672px;top:197px;width:221px">Letterhead</div>
<section class="piece sheet letterhead">
  <svg class="art" width="221" height="324" viewBox="0 0 221 324">
    <polygon points="150,300 221,262 221,324 130,324" fill="var(--blue)"/>
    <polygon points="170,290 221,262 221,268 178,291" fill="#fff"/>
  </svg>
  <div class="wordmark">RPB Builds</div>
  <div class="sheet-address">4827 Pelham Crescent<br>Edmonton, AB T6R 2J8<br>calvin@rpbbuilds.com</div>
  <div class="sheet-url">rpbbuilds.com</div>
</section>

<div class="piece-label" style="left:724px;top:76px;width:76px">Business Card Front</div>
<section class="piece card-v card-front">
  <svg class="art" width="60" height="108" viewBox="0 0 60 108">
    <polygon points="0,96 60,78 60,108 0,108" fill="var(--blue)"/>
  </svg>
  <div class="wordmark">RPB Builds</div>
  <div class="card-text"><b>Calvin Morrow, MBA</b><br>Owner<br>4827 Pelham Crescent<br>Edmonton, AB T6R 2J8<br>calvin@rpbbuilds.com</div>
</section>

<div class="piece-label" style="left:791px;top:76px;width:76px">Business Card Back</div>
<section class="piece card-v card-back">
  <svg class="art" width="60" height="108" viewBox="0 0 60 108">
    <polygon points="0,100 60,86 60,108 0,108" fill="var(--blue)"/>
  </svg>
  <div class="wordmark">RPB Builds</div>
</section>

<div class="piece-label" style="left:888px;top:76px;width:168px">E-mail Signature</div>
<section class="piece signature">
  <svg class="art" width="168" height="62" viewBox="0 0 168 62">
    <polygon points="90,62 168,40 168,62" fill="var(--blue)"/>
  </svg>
  <div class="card-text"><b>Calvin Morrow, MBA</b><br>Owner</div>
  <div class="wordmark">RPB Builds</div>
</section>

<div class="piece-label" style="left:924px;top:244px;width:132px">Mailing Label</div>
<section class="piece label">
  <svg class="art" width="132" height="74" viewBox="0 0 132 74">
    <polygon points="70,74 132,54 132,74" fill="var(--blue)"/>
  </svg>
  <div class="wordmark">RPB Builds</div>
  <div class="card-text">4827 Pelham Crescent<br>Edmonton, AB T6R 2J8</div>
</section>

<div class="piece-label" style="left:924px;top:347px;width:132px">Envelope</div>
<section class="piece envelope">
  <svg class="art" width="132" height="113" viewBox="0 0 132 113">
    <polyline points="0,0 66,52 132,0" fill="none" stroke="#d5d5d5" stroke-width="1"/>
    <polygon points="0,100 50,113 0,113" fill="var(--blue)"/>
  </svg>
  <div class="wordmark">RPB Builds</div>
  <div class="card-text">4827 Pelham Crescent<br>Edmonton, AB T6R 2J8</div>
</section>

</body>
</html>
```